Brochure Design: Text Messaging Service

We are looking for a brochure design for our new text messaging service. this should be a 2 page design on a 8.5x11" page
this should a clean design that catshed the eyey and features the features and benefits.
the brochure should bew designed so that we can entice our existing business clients to adopt this new service for their business.

Target Market(s)

business owner

Industry/Entity Type

Driving School

Font styles to use
Sans Serif

Colors
0692cd
33b8a4

Requirements
Must have
• pricing info, features, and screen shot on a computer. maybe also include image of your teen with cell phone.
Nice to have
• n/a
Should not have
• n/a

```html
<!DOCTYPE html>
<html lang="en">
<head>
<meta charset="utf-8">
<title>SMS Information Pamphlet – LaneWise Software</title>
<link rel="stylesheet" href="https://fonts.googleapis.com/css2?family=Source+Sans+3:wght@400;600;700&display=swap">
<style>
  :root {
    --backdrop: #ffbb5c;
    --paper: #ffffff;
    --ink: #1e1e1e;
    --body-ink: #2a2a2a;
    --muted: #666666;
    --brand-blue: #0692cd;
    --panel-blue: #0e8fcf;
    --band-light: #d9d9db;
    --band-dark: #b4b4b6;
    --icon-grey: #e4e4e4;
  }
  * { margin: 0; padding: 0; box-sizing: border-box; }
  html, body { width: 1200px; height: 900px; overflow: hidden; }
  body {
    background: var(--backdrop);
    font-family: "Source Sans 3", "Myriad Pro", Arial, sans-serif;
    color: var(--body-ink);
    position: relative;
  }
  .page {
    position: absolute;
    top: 20px;
    width: 570px;
    height: 740px;
    background: var(--paper);
    box-shadow: 2px 3px 6px rgba(0,0,0,.25);
    overflow: hidden;
  }
  .page--front { left: 23px; }
  .page--back { left: 608px; }

  .footer-band { position: absolute; left: 0; top: 630px; width: 570px; height: 110px; }
  .page-url {
    position: absolute; left: 32px; top: 690px;
    font-size: 10.5px; color: var(--muted); letter-spacing: .1px;
  }

  /* front page */
  .hero-photo {
    position: absolute; left: 0; top: 0; width: 570px; height: 385px;
    background: linear-gradient(135deg, #8a9a86 0%, #a9a296 35%, #6e7c8c 60%, #c9c2b8 100%);
  }
  .hero-cut { position: absolute; left: 0; top: 0; }
  .hero-tagline {
    position: absolute; left: 283px; top: 80px;
    font-size: 24px; font-weight: 700; color: #fff; font-style: italic;
    text-shadow: 0 1px 3px rgba(0,0,0,.45);
  }
  .brand-mark {
    position: absolute; left: 385px; top: 280px; width: 90px; height: 90px;
    border-radius: 50%; background: #fff;
    box-shadow: 0 1px 4px rgba(0,0,0,.2);
  }
  .brand-name {
    position: absolute; left: 295px; top: 378px; width: 245px; text-align: center;
    font-size: 28px; font-weight: 700; color: var(--brand-blue); line-height: 1.1;
    white-space: nowrap;
  }
  .brand-line {
    position: absolute; left: 295px; top: 434px; width: 245px; text-align: center;
    font-size: 7px; font-weight: 700; color: var(--ink); letter-spacing: .1px;
    white-space: nowrap;
  }
  .phone-icon { position: absolute; left: 370px; top: 480px; }
  .front-title {
    position: absolute; left: 31px; top: 404px;
    font-size: 37px; font-weight: 700; line-height: 38px; color: var(--ink);
    letter-spacing: .3px;
  }
  .front-intro {
    position: absolute; left: 32px; top: 542px; width: 506px;
    font-size: 15.5px; line-height: 19px; text-align: justify;
  }
  .front-intro strong { padding-left: 80px; font-weight: 700; color: var(--ink); }

  /* back page */
  .back-photo {
    position: absolute; inset: 0;
    background: linear-gradient(160deg, #f4f4f4 0%, #ececec 45%, #e2e2e2 100%);
  }
  .back-copy {
    position: absolute; left: 32px; width: 506px;
    font-size: 15px; line-height: 18.6px; text-align: justify; color: var(--body-ink);
  }
  .back-copy p + p { margin-top: 18px; }
  .back-copy--top { top: 44px; }
  .back-copy--bottom { top: 466px; }
  .feature-band { position: absolute; left: 0; top: 202px; width: 570px; height: 251px; display: flex; }
  .laptop-photo {
    width: 260px; height: 100%;
    background: linear-gradient(120deg, #d8d3cc 0%, #efeeec 40%, #8c8f94 70%, #e9e7e3 100%);
  }
  .feature-panel {
    flex: 1; background: var(--panel-blue);
    padding: 36px 0 0 18px;
  }
  .feature-list { list-style: none; color: #fff; font-size: 12.8px; line-height: 15.3px; }
  .feature-list li::before { content: "\2713"; margin-right: 6px; }
</style>
</head>
<body>

<section class="page page--front">
  <div class="hero-photo" role="img" aria-label="Photo of a parent and teen on a sofa looking at a mobile phone"></div>
  <svg class="hero-cut" width="570" height="400" aria-hidden="true">
    <path d="M0 385 L360 385 C430 385 470 320 570 250 L570 400 L0 400 Z" fill="var(--paper)"/>
  </svg>
  <div class="hero-tagline">“It’s the Driving School”</div>
  <div class="brand-mark"></div>
  <div class="brand-name">LaneWise Software</div>
  <div class="brand-line">ENROLLMENT - BILLING - SCHEDULING - REPORTING AND MORE</div>

  <svg class="phone-icon" width="96" height="190" aria-hidden="true">
    <rect x="4" y="4" width="88" height="182" rx="12" fill="none" stroke="var(--icon-grey)" stroke-width="6"/>
    <line x1="4" y1="32" x2="92" y2="32" stroke="var(--icon-grey)" stroke-width="4"/>
    <line x1="4" y1="150" x2="92" y2="150" stroke="var(--icon-grey)" stroke-width="4"/>
    <circle cx="48" cy="168" r="8" fill="none" stroke="var(--icon-grey)" stroke-width="4"/>
  </svg>

  <h1 class="front-title">SMS<br>INFORMATION<br>PAMFLET</h1>
  <p class="front-intro"><strong>SMS Communication Module</strong> is designed to allow your school to effectively communicate with both parent and students in near real-time. In today’s world, both students and parent expect almost instant communication with the service provider and driving schools.</p>

  <svg class="footer-band" viewBox="0 0 570 110" aria-hidden="true">
    <path d="M0 10 L570 70 L570 110 L0 110 Z" fill="var(--band-light)"/>
    <path d="M437 110 L570 40 L570 110 Z" fill="var(--band-dark)"/>
  </svg>
  <div class="page-url">www.lanewisesoftware.com</div>
</section>

<section class="page page--back">
  <div class="back-photo" role="img" aria-label="Faded background photo of a teen using a phone"></div>
  <div class="back-copy back-copy--top">
    <p>With our integrated SMS Messaging Module, you’re your school can automatically send reminders for classroom, in-car lessons, road tests, urgent notifications and more. Students and parent can also reply to those messages.</p>
    <p>Each school will be assigned a dedicated phone number, which could be either local number of your choice or toll-free number. Since this module is fully integrated the staff will not need to use any external or third party services to accomplish the same effect, hence saving time and money.</p>
  </div>

  <div class="feature-band">
    <div class="laptop-photo" role="img" aria-label="Laptop on a desk showing the SMS messaging screen of the software"></div>
    <div class="feature-panel">
      <ul class="feature-list">
        <li>Dedicated local or toll-free phone number</li>
        <li>Custom message content</li>
        <li>Delivery confirmation</li>
        <li>Two-way messaging</li>
        <li>On-Demand messaging</li>
        <li>Phone number validation</li>
        <li>Online enrollment integration</li>
        <li>Mass communication</li>
        <li>Plans starting at $25 / month for 500 messages</li>
        <li>Additional messages $.03 / message</li>
      </ul>
    </div>
  </div>

  <div class="back-copy back-copy--bottom">
    <p>Each SMS phone number is tracked individually and assigned to student account. During the enrollment process students and parents can opt to receive SMS notifications. However, at any point later on they can add or remove phone numbers for notifications.</p>
    <p>SMS Module is the first step in a very extensive list of features and capabilities that will be brought to to you. With plans starting at $25 / month, it is a very affordable solution for your school and business, while providing an efficient and cost effective communication tool.</p>
  </div>

  <svg class="footer-band" viewBox="0 0 570 110" aria-hidden="true">
    <path d="M0 10 L570 70 L570 110 L0 110 Z" fill="var(--band-light)"/>
    <path d="M437 110 L570 40 L570 110 Z" fill="var(--band-dark)"/>
  </svg>
  <div class="page-url">www.lanewisesoftware.com</div>
</section>

</body>
</html>
```